Flyer for Makeup Class

A flyer for my makeup class promotion. I am a make up artist starting a group class to teach makeup to ladies. I have attached some verbiage handwritten. My picture is the one in pink hijab. I have also attached some inspiration ideas and color combination (the colors in the cake design are the ones I want to use).

Target Market(s)

Ladies looking to learn make up from a make up artist

Industry/Entity Type

Hair And Beauty

Requirements
Must have
• The verbiage / description that I have hand written should be written using graphics and nice fonts. You can change the exact wording to make it better.

```html
<!DOCTYPE html>
<html lang="en">
<head>
<meta charset="utf-8">
<title>Exclusive Makeup Class Flyer</title>
<link href="https://fonts.googleapis.com/css2?family=Montserrat:wght@500;600;700;800&family=Playfair+Display:wght@600;700&display=swap" rel="stylesheet">
<style>
  :root {
    --backdrop: #ecebea;
    --pink: #ee5f9b;
    --pink-deep: #e23f86;
    --pink-soft: #f7a9c9;
    --blush: #fde6ef;
    --yellow: #fff147;
    --ink: #2b2b2b;
    --wine: #8a1d45;
    --white: #ffffff;
  }
  * { box-sizing: border-box; margin: 0; padding: 0; }
  html, body { width: 1200px; height: 798px; overflow: hidden; }
  body {
    background: var(--backdrop);
    font-family: "Montserrat", Arial, sans-serif;
    position: relative;
  }
  .flyer {
    position: absolute;
    left: 342px; top: 19px;
    width: 516px; height: 760px;
    overflow: hidden;
    background: linear-gradient(180deg, var(--white) 0%, var(--blush) 22%, var(--pink-soft) 55%, var(--pink) 100%);
    box-shadow: 0 6px 18px rgba(0,0,0,.18);
  }
  .flyer > * { position: absolute; }
  .kicker {
    top: 72px; left: 0; width: 100%;
    text-align: center;
    font-size: 23px; font-weight: 600; color: var(--ink);
  }
  .lipstick-art {
    top: 40px; left: 448px; width: 58px; height: 70px;
    border-radius: 8px;
    background: linear-gradient(160deg, #f7c6a3, #e9576f);
  }
  .artist-name {
    top: 112px; left: 0; width: 100%;
    text-align: center;
    font-size: 50px; font-weight: 800; letter-spacing: 2px;
    color: var(--pink);
  }
  .artist-title {
    top: 170px; left: 0; width: 100%;
    text-align: center;
    font-family: "Playfair Display", Georgia, serif;
    font-size: 18px; font-weight: 600; color: var(--ink);
  }
  .brush-art {
    top: 268px; left: 22px; width: 54px; height: 64px;
    border-radius: 6px;
    background: linear-gradient(160deg, #ffffff, #f28ab3);
  }
  .event-date {
    top: 210px; left: 56px; width: 166px;
    padding: 8px 0 10px;
    border-top: 2px solid var(--pink-deep);
    border-bottom: 2px solid var(--pink-deep);
    font-size: 16px; font-weight: 600; color: var(--ink); line-height: 1.4;
  }
  .divider {
    top: 212px; left: 234px; width: 2px; height: 58px;
    background: var(--pink-deep);
  }
  .event-venue {
    top: 218px; left: 250px; width: 230px;
    font-size: 16px; font-weight: 600; color: var(--ink); line-height: 1.4;
  }
  .audience-banner {
    top: 306px; left: 186px; width: 294px;
    padding: 9px 14px;
    background: var(--yellow);
    font-size: 13.5px; font-weight: 800; color: var(--ink);
    line-height: 1.3; text-transform: uppercase;
  }
  .portrait {
    top: 360px; left: 50px; width: 232px; height: 400px;
    border-radius: 120px 120px 0 0;
    background: linear-gradient(180deg, #f8d4dd 0%, #f2a6c2 55%, #e8739f 100%);
  }
  .class-details {
    top: 380px; left: 282px; width: 212px;
    font-family: "Playfair Display", Georgia, serif;
    font-size: 15px; font-weight: 700; line-height: 1.38;
    color: var(--wine);
  }
  .booking {
    top: 534px; left: 298px; width: 240px; height: 240px;
    border-radius: 50%;
    background: var(--yellow);
    padding: 48px 0 0 36px;
    color: var(--ink);
  }
  .booking-title {
    font-size: 15px; font-weight: 800; line-height: 1.3;
    text-transform: uppercase; margin-bottom: 10px;
  }
  .booking-line { font-size: 13px; font-weight: 700; line-height: 1.45; }
  .booking-label { font-size: 11px; font-weight: 700; text-transform: uppercase; margin-top: 6px; }
  .booking-handle { font-size: 11px; font-weight: 600; }
</style>
</head>
<body>
  <main class="flyer">
    <p class="kicker">Exclusive Makeup Class by</p>
    <div class="lipstick-art" role="img" aria-label="Illustration of a lipstick"></div>
    <h1 class="artist-name">SAMIRA NOOR</h1>
    <p class="artist-title">UK Based MUA</p>

    <div class="brush-art" role="img" aria-label="Illustration of makeup brushes"></div>
    <p class="event-date">April 6, 2019<br>11:30–5:30pm</p>
    <span class="divider"></span>
    <p class="event-venue">at the Lakeside Club Hall<br>(Riverton)</p>

    <p class="audience-banner">Perfect for professionals, beginners and make up lovers!</p>

    <div class="portrait" role="img" aria-label="Photo of the makeup artist in a pink hijab holding a compact"></div>

    <p class="class-details">This class is packed with loads of information tips, live demos, goodie bag, certificate, Q&amp;A/lunch and much more...</p>

    <section class="booking">
      <p class="booking-title">To book your<br>place contact</p>
      <p class="booking-line">07700 900 412</p>
      <p class="booking-line">0300 555 0186</p>
      <p class="booking-label">Instagram</p>
      <p class="booking-handle">@samiranoormua</p>
    </section>
  </main>
</body>
</html>
```